Real Estate Investment Company

Design Powerpoint slides are consistent with our logo, colors, and typeface. These Powerpoint slides will be used in all aspects of the business from live presentations to presentation decks available on a website or via email. Need to have different slide types created that allow for different types of slides such as cover pages, text heavy pages, image and chart heavy pages, multiple column pages, and mixed content pages.

Reason: to give additional time to get the design correct. I plan on making a selection in the next day or 2

Target Market(s)

Real Estate Investors

Industry/Entity Type

Investment

Other font styles liked:
• Consistent with logo

Requirements
Must have
• Our colors
• Our logo where possible
• Different slide designs of the same theme to allow for different types of slides such as cover pages, text heavy, picture heavy, and mixed content.
• Slides in both portrait and landscape orientation
Nice to have

```html
<!DOCTYPE html>
<html lang="en">
<head>
<meta charset="utf-8">
<title>PowerPoint Design Idea – Part 06</title>
<link href="https://fonts.googleapis.com/css2?family=Barlow+Condensed:wght@400;500&family=Montserrat:wght@400;600;800&family=Open+Sans:wght@400;600&family=Libre+Baskerville&display=swap" rel="stylesheet">
<style>
:root{
  --board:#050505;
  --heading:#a9d9e9;
  --navy:#1f3a64;
  --brand:#27508f;
  --blue:#4a78c2;
  --red:#d8402b;
  --orange:#f08a1c;
  --yellow:#f1c40f;
  --green:#3cb34a;
  --lime:#8cc152;
  --teal:#2b9aa6;
  --ink:#333;
  --copy:#8a8a8a;
}
*{margin:0;padding:0;box-sizing:border-box}
html,body{width:1200px;height:1200px;overflow:hidden;background:var(--board)}
.board{position:relative;width:1200px;height:1200px;font-family:"Open Sans",sans-serif}
.board-title{position:absolute;top:10px;left:0;width:1172px;text-align:center;font-family:"Barlow Condensed",sans-serif;font-weight:500;font-size:39px;letter-spacing:1px;color:var(--heading)}
.board-sub{position:absolute;top:84px;left:0;width:1216px;text-align:center;font-family:"Barlow Condensed",sans-serif;font-size:20px;line-height:29px;color:var(--heading);letter-spacing:.3px}
.slide{position:absolute;background:#fff;overflow:hidden}
.stage{position:absolute;left:0;top:0;width:840px;height:480px;transform-origin:0 0;transform:scale(var(--sx),var(--sy));box-shadow:inset 0 0 0 4px #e6e6e6}
.abs{position:absolute}
.brand{position:absolute;right:32px;bottom:12px;font-family:"Montserrat",sans-serif;font-weight:600;font-size:14px;color:var(--brand)}
.brand::before{content:"";display:inline-block;width:14px;height:14px;border-radius:50%;background:var(--brand);margin-right:6px;vertical-align:-2px}
.copy{font-size:10px;line-height:15px;color:var(--copy);text-align:justify}
.h-bold{font-family:"Montserrat",sans-serif;font-weight:800;font-size:24px;color:var(--ink)}
.h-mid{font-family:"Montserrat",sans-serif;font-weight:600;font-size:16px;color:var(--ink);text-align:center}
.h-thin{font-size:34px;color:var(--ink);text-align:center}
.h-blue{font-family:"Barlow Condensed",sans-serif;font-weight:500;font-size:28px;color:var(--brand);text-align:center}
.h-serif{font-family:"Libre Baskerville",serif;font-size:26px;color:var(--blue);text-align:center}
.kicker{font-size:12px;letter-spacing:8px;color:var(--red);font-family:"Montserrat",sans-serif}
.tag{display:inline-block;background:var(--green);color:#fff;font-family:"Montserrat",sans-serif;font-weight:800;font-size:12px;padding:5px 20px}
.ps-head{font-family:"Montserrat",sans-serif;font-weight:800;font-size:14px;color:#555;border-left:6px solid var(--brand);padding-left:12px}
.col-head{font-family:"Montserrat",sans-serif;font-weight:600;font-size:12px;color:#333;border-bottom:2px solid #999;padding-bottom:4px;margin-bottom:8px}
.pill{display:inline-block;background:var(--navy);color:#fff;font-size:12px;padding:7px 32px}
.layout-word{font-family:"Barlow Condensed",sans-serif;font-weight:500;font-size:38px;color:var(--ink);text-align:center}
.sub-red{font-size:11px;color:var(--red)}
.bar-label{font-size:10px;color:#fff;text-align:center;line-height:20px;height:20px}
.dbl-line{position:absolute;left:112px;right:112px;height:6px;background:linear-gradient(90deg,var(--orange) 0 12%,var(--navy) 12% 88%,var(--orange) 88%)}
.proj-name{font-family:"Libre Baskerville",serif;font-size:12px;color:#555;text-align:center}
</style>
</head>
<body>
<main class="board">
  <h1 class="board-title">POWERPOINT DESIGN IDEA (PART-06) [STILL WORKING]</h1>
  <p class="board-sub">THIS SUBMISSION CONTAINS TEXT FORMAT &nbsp;IDEAS ( STILL WORKING ON FORMATTING)<br>DESIGNED ON LIGHT BACKGROUND (WHITE) 16:9 FORMAT</p>

  <!-- Row 1 -->
  <section class="slide" style="left:10px;top:208px;width:214px;height:123px;--sx:.2548;--sy:.2563"><div class="stage">
    <div class="abs" style="left:0;right:0;top:60px;text-align:center;font-weight:600;font-size:30px;color:#666">Individual Skill</div>
    <div class="abs copy" style="left:200px;right:200px;top:104px;text-align:center;color:#ccc">Lorem ipsum dolor sit amet consectetur adipiscing</div>
    <div class="abs" role="img" aria-label="Portrait photo of team member" style="left:108px;top:160px;width:256px;height:276px;background:#b8b8b8"></div>
    <div class="abs" style="left:384px;top:160px;font-family:'Montserrat',sans-serif;font-weight:800;font-size:13px;color:var(--brand)">Marta Ellison</div>
    <div class="abs copy" style="left:384px;top:182px;width:400px">Lorem ipsum dolor sit amet, consectetur adipiscing elit sed do eiusmod tempor.</div>
    <svg class="abs" style="left:384px;top:232px" width="440" height="192" viewBox="0 0 110 48">
      <g font-size="2.4" fill="#999" font-family="Open Sans"><text x="0" y="4">HOSPITALITY</text><text x="0" y="14">DECORATION</text><text x="0" y="24">SKILL</text><text x="0" y="34">TECHNIQUE</text><text x="0" y="44">CREATIVE</text></g>
      <g fill="var(--red)"><circle cx="30" cy="3" r="2.6"/><circle cx="37" cy="3" r="2.6"/><circle cx="44" cy="3" r="2.6"/><circle cx="51" cy="3" r="2.6"/><circle cx="58" cy="3" r="2.6"/><circle cx="65" cy="3" r="2.6"/><circle cx="72" cy="3" r="2.6"/></g>
      <g fill="#ccc"><circle cx="79" cy="3" r="2.6"/><circle cx="86" cy="3" r="2.6"/><circle cx="93" cy="3" r="2.6"/></g>
      <g fill="var(--orange)"><circle cx="30" cy="13" r="2.6"/><circle cx="37" cy="13" r="2.6"/><circle cx="44" cy="13" r="2.6"/><circle cx="51" cy="13" r="2.6"/><circle cx="58" cy="13" r="2.6"/><circle cx="65" cy="13" r="2.6"/></g>
      <g fill="#ccc"><circle cx="72" cy="13" r="2.6"/><circle cx="79" cy="13" r="2.6"/><circle cx="86" cy="13" r="2.6"/><circle cx="93" cy="13" r="2.6"/></g>
      <g fill="var(--yellow)"><circle cx="30" cy="23" r="2.6"/><circle cx="37" cy="23" r="2.6"/><circle cx="44" cy="23" r="2.6"/><circle cx="51" cy="23" r="2.6"/><circle cx="58" cy="23" r="2.6"/><circle cx="65" cy="23" r="2.6"/><circle cx="72" cy="23" r="2.6"/><circle cx="79" cy="23" r="2.6"/></g>
      <g fill="#ccc"><circle cx="86" cy="23" r="2.6"/><circle cx="93" cy="23" r="2.6"/></g>
      <g fill="var(--green)"><circle cx="30" cy="33" r="2.6"/><circle cx="37" cy="33" r="2.6"/><circle cx="44" cy="33" r="2.6"/><circle cx="51" cy="33" r="2.6"/><circle cx="58" cy="33" r="2.6"/><circle cx="65" cy="33" r="2.6"/><circle cx="72" cy="33" r="2.6"/></g>
      <g fill="#ccc"><circle cx="79" cy="33" r="2.6"/><circle cx="86" cy="33" r="2.6"/><circle cx="93" cy="33" r="2.6"/></g>
      <g fill="var(--teal)"><circle cx="30" cy="43" r="2.6"/><circle cx="37" cy="43" r="2.6"/><circle cx="44" cy="43" r="2.6"/><circle cx="51" cy="43" r="2.6"/><circle cx="58" cy="43" r="2.6"/><circle cx="65" cy="43" r="2.6"/></g>
      <g fill="#ccc"><circle cx="72" cy="43" r="2.6"/><circle cx="79" cy="43" r="2.6"/><circle cx="86" cy="43" r="2.6"/><circle cx="93" cy="43" r="2.6"/></g>
    </svg>
    <span class="brand">Keystead</span>
  </div></section>

  <section class="slide" style="left:252px;top:208px;width:211px;height:123px;--sx:.2512;--sy:.2563"><div class="stage">
    <div class="abs" style="left:40px;right:40px;top:44px;height:272px;background:var(--navy)"></div>
    <div class="abs" style="left:340px;top:80px;font-size:14px;color:#fff">Lena Harwick</div>
    <div class="abs" style="left:340px;top:100px;font-size:10px;color:#9fb3d1">Founder</div>
    <div class="abs copy" style="left:340px;top:120px;width:390px;color:#b7c4d8">Lorem ipsum dolor sit amet, consectetur adipiscing elit, sed do eiusmod tempor incididunt ut labore et dolore magna aliqua ut enim ad minim veniam.</div>
    <svg class="abs" style="left:340px;top:208px" width="240" height="88" viewBox="0 0 60 22"><circle cx="2.5" cy="2.5" r="2" fill="var(--yellow)"/><circle cx="2.5" cy="9.5" r="2" fill="var(--orange)"/><circle cx="2.5" cy="16.5" r="2" fill="var(--blue)"/><g fill="#b7c4d8"><rect x="7" y="2" width="30" height="1"/><rect x="7" y="9" width="22" height="1"/><rect x="7" y="16" width="26" height="1"/></g></svg>
    <div class="abs sub-red" style="left:88px;top:344px">Skill Development</div>
    <div class="abs copy" style="left:88px;top:364px;width:216px">Lorem ipsum dolor sit amet consectetur adipiscing elit sed do.</div>
    <svg class="abs" style="left:328px;top:352px" width="280" height="80" viewBox="0 0 70 20"><rect y="0" width="48" height="1.8" fill="var(--yellow)"/><rect y="4" width="58" height="1.8" fill="var(--orange)"/><rect y="8" width="40" height="1.8" fill="var(--teal)"/><rect y="12" width="52" height="1.8" fill="var(--blue)"/><rect y="16" width="34" height="1.8" fill="var(--green)"/></svg>
    <span class="brand">Keystead</span>
  </div></section>

  <section class="slide" style="left:491px;top:208px;width:211px;height:123px;--sx:.2512;--sy:.2563"><div class="stage">
    <div class="abs" style="left:0;right:0;top:74px;text-align:center;font-family:'Montserrat',sans-serif;font-weight:800;font-size:18px;color:#222">MEET OWEN CARTER</div>
    <div class="abs copy" style="left:240px;right:240px;top:100px;text-align:center">Lorem ipsum dolor sit amet consectetur adipiscing elit sed do</div>
    <div class="abs" style="left:168px;top:180px;font-size:12px;color:#555">Who is this?</div>
    <div class="abs copy" style="left:168px;top:204px;width:264px">Lorem ipsum dolor sit amet, consectetur adipiscing elit, sed do eiusmod tempor incididunt ut labore et dolore magna aliqua. Ut enim ad minim veniam, quis nostrud exercitation ullamco laboris nisi ut aliquip ex ea commodo consequat.</div>
    <div class="abs" style="left:176px;top:380px;font-size:10px;color:var(--brand);font-weight:600">OWEN CARTER</div>
    <div class="abs" style="left:532px;top:180px;font-size:12px;color:#555">Skill:</div>
    <svg class="abs" style="left:532px;top:212px" width="240" height="160" viewBox="0 0 60 40"><defs><pattern id="stripe" width="2" height="2" patternUnits="userSpaceOnUse" patternTransform="rotate(45)"><rect width="1" height="2" fill="var(--orange)"/></pattern></defs>
      <rect y="0" width="34" height="2.4" fill="url(#stripe)"/><rect y="8" width="28" height="2.4" fill="url(#stripe)"/><rect y="16" width="36" height="2.4" fill="url(#stripe)"/><rect y="24" width="30" height="2.4" fill="url(#stripe)"/><rect y="32" width="38" height="2.4" fill="var(--brand)"/>
      <g font-size="2.6" fill="var(--orange)"><text x="46" y="2.5">25%</text><text x="46" y="10.5">30%</text><text x="46" y="18.5">50%</text><text x="46" y="26.5">55%</text><text x="46" y="34.5">85%</text></g></svg>
    <span class="brand">Keystead</span>
  </div></section>

  <section class="slide" style="left:738px;top:208px;width:203px;height:123px;--sx:.2417;--sy:.2563"><div class="stage">
    <div class="abs" style="left:0;right:0;top:280px;text-align:center"><span class="pill">Now... Lets talk about...</span></div>
    <div class="abs layout-word" style="left:0;right:0;top:334px">TEXT LAYOUTS</div>
    <span class="brand">Keystead</span>
  </div></section>

  <section class="slide" style="left:976px;top:208px;width:214px;height:123px;--sx:.2548;--sy:.2563"><div class="stage">
    <div class="abs ps-head" style="left:80px;top:96px">PARAGRAPH STYLES</div>
    <div class="abs copy" style="left:80px;top:136px;width:330px">Lorem ipsum is simply dummy text of the printing and typesetting industry. Lorem ipsum has been the industry standard dummy text ever since the fifteen hundreds, when an unknown printer took a galley of type and scrambled it to make a type specimen book. It has survived not only five centuries but also the leap into electronic typesetting, remaining essentially unchanged.</div>
    <div class="abs copy" style="left:440px;top:136px;width:330px">Lorem ipsum is simply dummy text of the printing and typesetting industry. It has been the standard dummy text ever since.</div>
    <div class="abs copy" style="left:440px;top:180px;width:330px;background:var(--navy);color:#dbe3f0;padding:6px 10px">The standard chunk of lorem ipsum used since the fifteen hundreds is reproduced below for those interested readers.</div>
    <div class="abs copy" style="left:440px;top:240px;width:330px">Contrary to popular belief, lorem ipsum is not simply random text. It has roots in classical literature, making it over two thousand years old.</div>
    <div class="abs" style="left:440px;top:400px;width:330px;height:3px;background:var(--blue)"></div>
    <span class="brand">Keystead</span>
  </div></section>

  <!-- Row 2 -->
  <section class="slide" style="left:10px;top:346px;width:214px;height:120px;--sx:.2548;--sy:.25"><div class="stage">
    <div class="abs h-bold" style="left:112px;top:84px">DOUBLE ROW SLIDE</div>
    <div class="abs kicker" style="left:112px;top:116px">TEXT SLIDE</div>
    <div class="abs sub-red" style="left:112px;top:150px">Your Subtitle Here</div>
    <div class="abs copy" style="left:112px;top:168px;width:640px">Lorem ipsum dolor sit amet, consectetur adipiscing elit. Nam porttitor augue non purus ultrices pretium. Donec fermentum tempor suscipit vehicula dictum. Sed ultricies nulla at scelerisque tincidunt, vehicula sit amet neque posuere, eleifend dui sed tortor. Phasellus nec massa quis neque consequat gravida. Vivamus nec nisl ante.</div>
    <div class="abs sub-red" style="left:112px;top:270px">Your Subtitle Here</div>
    <div class="abs copy" style="left:112px;top:288px;width:640px">Lorem ipsum dolor sit amet, consectetur adipiscing elit. Nam porttitor augue non purus ultrices pretium. Donec fermentum tempor suscipit vehicula dictum. Sed ultricies nulla at scelerisque tincidunt, vehicula sit amet neque posuere, eleifend dui sed tortor. Phasellus nec massa quis neque consequat gravida. Vivamus nec nisl ante.</div>
    <span class="brand">Keystead</span>
  </div></section>

  <section class="slide" style="left:252px;top:346px;width:211px;height:120px;--sx:.2512;--sy:.25"><div class="stage">
    <div class="abs h-bold" style="left:112px;top:84px">NUMBER POINTS</div>
    <div class="abs kicker" style="left:112px;top:116px">TEXT SLIDE</div>
    <svg class="abs" style="left:112px;top:160px" width="640" height="224" viewBox="0 0 160 56" font-family="Montserrat">
      <g fill="var(--red)" font-size="5" font-weight="600"><text x="0" y="6">1</text><text x="55" y="6">2</text><text x="110" y="6">3</text><text x="0" y="26">4</text><text x="55" y="26">5</text><text x="110" y="26">6</text><text x="0" y="46">7</text><text x="55" y="46">8</text><text x="110" y="46">9</text></g>
      <g fill="#888" font-size="2.5" font-family="Open Sans">
        <text x="7" y="3">Lorem ipsum dolor sit amet,</text><text x="7" y="6.5">consectetur adipiscing elit.</text><text x="7" y="10">Nam porttitor augue.</text>
        <text x="62" y="3">Lorem ipsum dolor sit amet,</text><text x="62" y="6.5">consectetur adipiscing elit.</text><text x="62" y="10">Nam porttitor augue.</text>
        <text x="117" y="3">Lorem ipsum dolor sit amet,</text><text x="117" y="6.5">consectetur adipiscing elit.</text><text x="117" y="10">Nam porttitor augue.</text>
        <text x="7" y="23">Lorem ipsum dolor sit amet,</text><text x="7" y="26.5">consectetur adipiscing elit.</text><text x="7" y="30">Nam porttitor augue.</text>
        <text x="62" y="23">Lorem ipsum dolor sit amet,</text><text x="62" y="26.5">consectetur adipiscing elit.</text><text x="62" y="30">Nam porttitor augue.</text>
        <text x="117" y="23">Lorem ipsum dolor sit amet,</text><text x="117" y="26.5">consectetur adipiscing elit.</text><text x="117" y="30">Nam porttitor augue.</text>
        <text x="7" y="43">Lorem ipsum dolor sit amet,</text><text x="7" y="46.5">consectetur adipiscing elit.</text><text x="7" y="50">Nam porttitor augue.</text>
        <text x="62" y="43">Lorem ipsum dolor sit amet,</text><text x="62" y="46.5">consectetur adipiscing elit.</text><text x="62" y="50">Nam porttitor augue.</text>
        <text x="117" y="43">Lorem ipsum dolor sit amet,</text><text x="117" y="46.5">consectetur adipiscing elit.</text><text x="117" y="50">Nam porttitor augue.</text>
      </g></svg>
    <span class="brand">Keystead</span>
  </div></section>

  <section class="slide" style="left:491px;top:346px;width:211px;height:120px;--sx:.2512;--sy:.25"><div class="stage">
    <div class="abs" style="left:48px;top:60px"><span class="tag">PARAGRAPH STYLES</span></div>
    <div class="abs" style="left:120px;top:140px;width:290px"><div class="col-head">TWO COLUMN</div><div class="copy">Lorem ipsum is simply dummy text of the printing and typesetting industry. Lorem ipsum has been the industry standard dummy text ever since the fifteen hundreds, when an unknown printer took a galley of type and scrambled it to make a type specimen book. It has survived five centuries and the leap into electronic typesetting. It is a long established fact that a reader will be distracted by the readable content of a page when looking at its layout.</div></div>
    <div class="abs" style="left:448px;top:140px;width:290px"><div class="col-head">TWO COLUMN</div><div class="copy">Lorem ipsum is simply dummy text of the printing and typesetting industry. Lorem ipsum has been the industry standard dummy text ever since the fifteen hundreds, when an unknown printer took a galley of type and scrambled it to make a type specimen book. It has survived five centuries and the leap into electronic typesetting. It is a long established fact that a reader will be distracted by the readable content of a page when looking at its layout.</div></div>
    <span class="brand">Keystead</span>
  </div></section>

  <section class="slide" style="left:738px;top:346px;width:203px;height:120px;--sx:.2417;--sy:.25"><div class="stage">
    <div class="abs ps-head" style="left:80px;top:96px">PARAGRAPH STYLES</div>
    <div class="abs copy" style="left:80px;top:136px;width:210px">Lorem ipsum is simply dummy text of the printing and typesetting industry. It has been the standard dummy text ever since the fifteen hundreds, when a printer took a galley of type and scrambled it to make a specimen book. It has survived five centuries and the leap into typesetting.</div>
    <div class="abs copy" style="left:312px;top:136px;width:210px">Various versions have evolved over the years, sometimes by accident, sometimes on purpose. Contrary to popular belief, lorem ipsum is not simply random text. It has roots in classical literature, making it over two thousand years old.</div>
    <div class="abs copy" style="left:544px;top:136px;width:210px">The standard chunk used since the fifteen hundreds is reproduced below for those interested. Many desktop publishing packages and web page editors now use it as their default model text, and a search will uncover many sites.</div>
    <span class="brand">Keystead</span>
  </div></section>

  <section class="slide" style="left:976px;top:346px;width:214px;height:120px;--sx:.2548;--sy:.25"><div class="stage">
    <div class="abs" style="left:48px;top:60px"><span class="tag">PARAGRAPH STYLES</span></div>
    <div class="abs" style="left:112px;top:140px;width:196px"><div class="col-head">THREE COLUMN</div><div class="copy">Lorem ipsum is simply dummy text of the printing and typesetting industry. It has been the standard dummy text ever since the fifteen hundreds, when a printer took a galley of type and scrambled it to make a specimen book.</div></div>
    <div class="abs" style="left:332px;top:140px;width:196px"><div class="col-head">THREE COLUMN</div><div class="copy">Lorem ipsum is simply dummy text of the printing and typesetting industry. It has been the standard dummy text ever since the fifteen hundreds, when a printer took a galley of type and scrambled it to make a specimen book.</div></div>
    <div class="abs" style="left:552px;top:140px;width:196px"><div class="col-head">THREE COLUMN</div><div class="copy">Lorem ipsum is simply dummy text of the printing and typesetting industry. It has been the standard dummy text ever since the fifteen hundreds, when a printer took a galley of type and scrambled it to make a specimen book.</div></div>
    <span class="brand">Keystead</span>
  </div></section>

  <!-- Row 3 -->
  <section class="slide" style="left:10px;top:475px;width:214px;height:120px;--sx:.2548;--sy:.25"><div class="stage">
    <div class="abs h-mid" style="left:0;right:0;top:88px">DOUBLE COLUMN SLIDE</div>
    <div class="abs bar-label" style="left:188px;top:176px;width:208px;background:var(--yellow)">Subtitle</div>
    <div class="abs bar-label" style="left:448px;top:176px;width:208px;background:var(--lime)">Subtitle</div>
    <div class="abs copy" style="left:188px;top:212px;width:208px">Image wide array dusk trees, reflection of the glass tower high sitting. Lorem ipsum dolor sit amet, consectetur adipiscing elit sed do eiusmod tempor incididunt ut labore et dolore magna aliqua.</div>
    <div class="abs copy" style="left:448px;top:212px;width:208px">Image wide array dusk trees, reflection of the glass tower high sitting. Lorem ipsum dolor sit amet, consectetur adipiscing elit sed do eiusmod tempor incididunt ut labore et dolore magna aliqua.</div>
    <span class="brand">Keystead</span>
  </div></section>

  <section class="slide" style="left:252px;top:475px;width:211px;height:120px;--sx:.2512;--sy:.25"><div class="stage">
    <div class="abs h-mid" style="left:0;right:0;top:88px">TRIPLE COLUMN SLIDE</div>
    <div class="abs bar-label" style="left:228px;top:176px;width:128px;background:var(--yellow)">Subtitle</div>
    <div class="abs bar-label" style="left:384px;top:176px;width:128px;background:var(--blue)">Subtitle</div>
    <div class="abs bar-label" style="left:540px;top:176px;width:128px;background:var(--lime)">Subtitle</div>
    <div class="abs copy" style="left:228px;top:212px;width:128px">Image wide array dusk trees, reflection of the glass tower sitting high. Lorem ipsum dolor sit amet, consectetur adipiscing elit sed do.</div>
    <div class="abs copy" style="left:384px;top:212px;width:128px">Image wide array dusk trees, reflection of the glass tower sitting high. Lorem ipsum dolor sit amet, consectetur adipiscing elit sed do.</div>
    <div class="abs copy" style="left:540px;top:212px;width:128px">Image wide array dusk trees, reflection of the glass tower sitting high. Lorem ipsum dolor sit amet, consectetur adipiscing elit sed do.</div>
    <span class="brand">Keystead</span>
  </div></section>

  <section class="slide" style="left:491px;top:475px;width:211px;height:120px;--sx:.2512;--sy:.25"><div class="stage">
    <div class="abs h-mid" style="left:0;right:0;top:88px">DOUBLE ROW SLIDE</div>
    <div class="abs" style="left:0;right:0;top:144px;text-align:center;font-size:10px;color:var(--orange)">Subtitle</div>
    <div class="abs copy" style="left:200px;top:164px;width:448px;text-align:center">Image wide array dusk trees, reflection of the glass tower high sitting. Lorem ipsum dolor sit amet, consectetur adipiscing elit sed do eiusmod tempor incididunt ut labore et dolore magna aliqua ut enim minim veniam, quis nostrud exercitation.</div>
    <div class="abs" style="left:0;right:0;top:264px;text-align:center;font-size:10px;color:var(--orange)">Subtitle</div>
    <div class="abs copy" style="left:200px;top:284px;width:448px;text-align:center">Image wide array dusk trees, reflection of the glass tower high sitting. Lorem ipsum dolor sit amet, consectetur adipiscing elit sed do eiusmod tempor incididunt ut labore et dolore magna aliqua ut enim minim veniam, quis nostrud exercitation.</div>
    <span class="brand">Keystead</span>
  </div></section>

  <section class="slide" style="left:738px;top:475px;width:203px;height:120px;--sx:.2417;--sy:.25"><div class="stage">
    <div class="abs" style="left:0;right:0;top:50px;text-align:center;font-size:9px;color:var(--red)">CORPORATE SLIDES</div>
    <div class="abs h-blue" style="left:0;right:0;top:62px">TEXT IN ONE COLUMN</div>
    <div class="abs copy" style="left:80px;top:128px;width:680px">Marketing is about to thinking about the business in terms of customer needs and their satisfaction. Marketing differs from selling because selling concerns itself with the tricks and techniques of getting people to exchange their cash for your product. It is not concerned with the values that the exchange is all about, and it does not view the business as an integrated effort to satisfy customer needs.</div>
    <div class="abs copy" style="left:80px;top:226px;width:680px">Marketing is about to thinking about the business in terms of customer needs and their satisfaction. Marketing differs from selling because selling concerns itself with the tricks and techniques of getting people to exchange their cash for your product. It is not concerned with the values that the exchange is all about, and it does not view the business as an integrated effort to satisfy customer needs.</div>
    <div class="abs copy" style="left:80px;top:324px;width:680px">Marketing is about to thinking about the business in terms of customer needs and their satisfaction. Marketing differs from selling because selling concerns itself with the tricks and techniques of getting people to exchange their cash for your product and services.</div>
    <span class="brand">Keystead</span>
  </div></section>

  <section class="slide" style="left:976px;top:475px;width:214px;height:120px;--sx:.2548;--sy:.25"><div class="stage">
    <div class="abs" style="left:0;right:0;top:50px;text-align:center;font-family:'Barlow Condensed',sans-serif;font-size:22px;color:#333">ONE COLUMN LAYOUT</div>
    <div class="abs" style="left:72px;top:92px;font-size:10px;color:#555">&lsaquo; &nbsp;Cutting Edge PowerPoint Template</div>
    <div class="abs copy" style="left:112px;top:128px;width:664px">The new modern progressive framework lets you work towards the smart business template incorporating a big gateway of image and text, fine profile and fast readability. Whether the designers want more texts or short words, this template can manage a balance of content for attentive readers.</div>
    <div class="abs copy" style="left:112px;top:208px;width:664px">Designed with a clear grid and soft colours, every section keeps the reader focused on what matters most. Whether you present in a boardroom or share by email, the layout stays clean, steady and easy to follow through all slides of the deck.</div>
    <div class="abs copy" style="left:112px;top:288px;width:664px">The new modern progressive framework lets you work towards the smart business template incorporating a big gateway of image and text, fine profile and fast readability. Whether the designers want more texts or short words, this template can manage a balance of content.</div>
    <span class="brand">Keystead</span>
  </div></section>

  <!-- Row 4 -->
  <section class="slide" style="left:10px;top:607px;width:214px;height:116px;--sx:.2548;--sy:.2417"><div class="stage">
    <div class="abs" style="left:0;right:0;top:50px;text-align:center;font-size:9px;color:var(--red)">CORPORATE SLIDES</div>
    <div class="abs h-blue" style="left:0;right:0;top:62px">TEXT IN TWO COLUMNS</div>
    <div class="abs copy" style="left:112px;top:128px;width:300px">Marketing is about to thinking about the business in terms of customer needs and their satisfaction. Marketing differs from selling because selling concerns itself with the tricks and techniques of getting people to exchange their cash for your product. It is not concerned with the values that the exchange is all about.</div>
    <div class="abs copy" style="left:448px;top:128px;width:300px">Comprehensive advertising of goods, domain and destination marketing, business, hotel and tourism. Marketing is about to thinking about the business in terms of customer needs and their satisfaction. Selling concerns itself with getting people to exchange their cash for a product.</div>
    <span class="brand">Keystead</span>
  </div></section>

  <section class="slide" style="left:252px;top:607px;width:211px;height:116px;--sx:.2512;--sy:.2417"><div class="stage">
    <div class="abs h-thin" style="left:0;right:0;top:46px">TWO COLUMN LAYOUT</div>
    <div class="abs copy" style="left:0;right:0;top:98px;text-align:center;color:#bbb">Cutting Edge PowerPoint Template</div>
    <div class="abs copy" style="left:104px;top:140px;width:300px">The new modern progressive framework lets you work towards the smart business template incorporating a big gateway of image and text, fine profile and fast readability. Whether the designers want more texts or short words, this template can manage a balance of content. Create a unique presentation with new features.</div>
    <div class="abs copy" style="left:440px;top:140px;width:300px">The new modern progressive framework lets you work towards the smart business template incorporating a big gateway of image and text, fine profile and fast readability. Whether the designers want more texts or short words, this template can manage a balance of content. Create a unique presentation with new features.</div>
    <span class="brand">Keystead</span>
  </div></section>

  <section class="slide" style="left:491px;top:607px;width:211px;height:116px;--sx:.2512;--sy:.2417"><div class="stage">
    <div class="abs" style="left:0;right:0;top:50px;text-align:center;font-size:9px;color:var(--red)">CORPORATE SLIDES</div>
    <div class="abs h-blue" style="left:0;right:0;top:62px">TEXT IN THREE COLUMNS</div>
    <div class="abs copy" style="left:104px;top:128px;width:196px">Marketing is about to thinking about the business in terms of customer needs and their satisfaction. Marketing differs from selling because selling concerns itself with getting people to exchange their cash for your product.</div>
    <div class="abs copy" style="left:324px;top:128px;width:196px">Growth, sales and market share: marketing is about to thinking about the business in terms of customer needs and their satisfaction, not the tricks of selling to people.</div>
    <div class="abs copy" style="left:544px;top:128px;width:196px">In terms of customer needs and their satisfaction, marketing differs from selling because selling concerns itself with techniques, not with the values of the exchange.</div>
    <span class="brand">Keystead</span>
  </div></section>

  <section class="slide" style="left:738px;top:607px;width:203px;height:116px;--sx:.2417;--sy:.2417"><div class="stage">
    <div class="abs h-thin" style="left:0;right:0;top:46px">THREE COLUMN LAYOUT</div>
    <div class="abs copy" style="left:0;right:0;top:98px;text-align:center;color:#bbb">Cutting Edge PowerPoint Template</div>
    <div class="abs copy" style="left:72px;top:140px;width:208px">The new modern progressive framework lets you work towards the smart business template incorporating a big gateway of image and text, fine profile and fast readability. Whether designers want more text or short words, it keeps a balance.</div>
    <div class="abs copy" style="left:308px;top:140px;width:208px">The new modern progressive framework lets you work towards the smart business template incorporating a big gateway of image and text, fine profile and fast readability. Whether designers want more text or short words, it keeps a balance.</div>
    <div class="abs copy" style="left:544px;top:140px;width:208px">The new modern progressive framework lets you work towards the smart business template incorporating a big gateway of image and text, fine profile and fast readability. Whether designers want more text or short words, it keeps a balance.</div>
    <span class="brand">Keystead</span>
  </div></section>

  <section class="slide" style="left:976px;top:607px;width:214px;height:116px;--sx:.2548;--sy:.2417"><div class="stage">
    <div class="abs h-thin" style="left:0;right:0;top:46px">TWO COLUMNS WITH PICTURE</div>
    <div class="abs copy" style="left:0;right:0;top:98px;text-align:center;color:#bbb">Cutting Edge PowerPoint Template</div>
    <div class="abs" role="img" aria-label="Photo of a desk with phone and earphones" style="left:72px;top:136px;width:344px;height:224px;background:linear-gradient(135deg,#d9dde2,#8a929c 60%,#c7cbd0)"></div>
    <div class="abs" style="left:448px;top:156px;font-size:12px;color:#444">Northgate Studio is Digital Agency</div>
    <div class="abs copy" style="left:448px;top:180px;width:336px">Lorem ipsum dolor sit amet, consectetur adipiscing elit, sed do eiusmod tempor incididunt ut labore et dolore magna aliqua. Ut enim ad minim veniam, quis nostrud exercitation ullamco laboris nisi ut aliquip ex ea commodo consequat.</div>
    <div class="abs copy" style="left:448px;top:276px;width:336px">Excepteur sint occaecat cupidatat non proident, sunt in culpa qui officia deserunt mollit anim id est laborum.</div>
    <span class="brand">Keystead</span>
  </div></section>

  <!-- Row 5 -->
  <section class="slide" style="left:10px;top:734px;width:214px;height:126px;--sx:.2548;--sy:.2625"><div class="stage">
    <div class="abs" role="img" aria-label="Photo of a modern office interior in blue tones" style="left:48px;top:48px;width:480px;height:384px;background:linear-gradient(160deg,#3f6fb4,#2c5594)"></div>
    <div class="abs" style="left:80px;top:380px;width:224px;height:14px;background:#4aa3df"></div>
    <div class="abs" style="left:528px;top:48px;width:280px;height:384px;background:var(--navy)"></div>
    <div class="abs" style="left:552px;top:76px;font-family:'Montserrat',sans-serif;font-weight:800;font-size:14px;color:#fff">WHO WE ARE?</div>
    <div class="abs copy" style="left:552px;top:104px;width:232px;color:#b7c4d8">Lorem ipsum dolor sit amet, consectetur adipiscing elit, sed do eiusmod tempor incididunt ut labore et dolore magna aliqua. Ut enim ad minim veniam, quis nostrud exercitation ullamco laboris nisi ut aliquip ex ea commodo consequat. Duis aute irure dolor in reprehenderit in voluptate velit esse cillum dolore eu fugiat nulla pariatur. Excepteur sint occaecat cupidatat non proident, sunt in culpa qui officia deserunt mollit anim id est laborum.</div>
    <span class="brand" style="bottom:8px">Keystead</span>
  </div></section>

  <section class="slide" style="left:252px;top:734px;width:211px;height:126px;--sx:.2512;--sy:.2625"><div class="stage">
    <svg class="abs" style="left:80px;top:72px" width="120" height="120"><path d="M4 112V4H104" fill="none" stroke="var(--red)" stroke-width="9"/></svg>
    <div class="abs" style="left:200px;top:124px;width:456px;height:200px;background:#777;text-align:center;padding-top:66px">
      <div style="font-family:'Montserrat',sans-serif;font-weight:800;font-size:32px;color:#fff">SECTION BREAK</div>
      <div style="font-size:14px;letter-spacing:12px;color:#ddd">YOUR TITLE</div>
    </div>
    <div class="abs" style="left:40px;right:40px;top:416px;height:40px;background:linear-gradient(90deg,#f6a623,var(--orange) 50%,var(--red))"></div>
    <div class="abs" style="left:660px;top:427px;font-family:'Montserrat',sans-serif;font-weight:600;font-size:14px;letter-spacing:6px;color:#fff">KEYSTEAD</div>
  </div></section>

  <section class="slide" style="left:491px;top:734px;width:211px;height:126px;--sx:.2512;--sy:.2625"><div class="stage">
    <div class="abs" style="left:292px;top:120px;width:272px;height:272px;border-radius:50%;background:var(--blue);text-align:center;padding-top:104px">
      <div style="font-family:'Montserrat',sans-serif;font-weight:800;font-size:36px;color:#fff">BREAK</div>
      <div style="font-size:9px;color:#dbe5f5">Presentation break area</div>
    </div>
    <span class="brand">Keystead</span>
  </div></section>

  <section class="slide" style="left:738px;top:734px;width:203px;height:126px;--sx:.2417;--sy:.2625"><div class="stage">
    <div class="abs" style="left:0;right:0;top:280px;text-align:center"><span class="pill">Now... Lets talk about...</span></div>
    <div class="abs layout-word" style="left:0;right:0;top:334px">PROJECT GALLERY</div>
    <span class="brand">Keystead</span>
  </div></section>

  <section class="slide" style="left:976px;top:734px;width:214px;height:126px;--sx:.2548;--sy:.2625"><div class="stage">
    <div class="abs h-serif" style="left:24px;width:480px;top:80px;color:#777">AGENDA IDEA – 04</div>
    <div class="abs copy" style="left:80px;width:368px;top:116px;text-align:center">Lorem ipsum dolor sit amet, consectetur adipiscing elit sed do eiusmod.</div>
    <div class="abs" role="img" aria-label="Black and white photo of a tall windowed hall" style="left:512px;top:48px;width:304px;height:400px;background:linear-gradient(120deg,#2d2d2d,#8c8c8c 55%,#3a3a3a)"></div>
    <svg class="abs" style="left:64px;top:172px" width="440" height="240" viewBox="0 0 110 60" font-family="Open Sans">
      <g fill="var(--brand)"><circle cx="6" cy="6" r="5"/><circle cx="6" cy="26" r="5"/><circle cx="6" cy="46" r="5"/><circle cx="56" cy="6" r="5"/><circle cx="56" cy="26" r="5"/><circle cx="56" cy="46" r="5"/></g>
      <g font-size="2.4" fill="#333"><text x="14" y="3">INTRODUCTION</text><text x="14" y="23">CONCEPT</text><text x="14" y="43">PERFORMANCE</text><text x="64" y="3">ABOUT US</text><text x="64" y="23">SEARCH</text><text x="64" y="43">CONTACT US</text></g>
      <g font-size="2.1" fill="#999"><text x="14" y="7">Lorem ipsum dolor sit</text><text x="14" y="10">amet consectetur.</text><text x="14" y="27">Lorem ipsum dolor sit</text><text x="14" y="30">amet consectetur.</text><text x="14" y="47">Lorem ipsum dolor sit</text><text x="14" y="50">amet consectetur.</text><text x="64" y="7">Lorem ipsum dolor sit</text><text x="64" y="10">amet consectetur.</text><text x="64" y="27">Lorem ipsum dolor sit</text><text x="64" y="30">amet consectetur.</text><text x="64" y="47">Lorem ipsum dolor sit</text><text x="64" y="50">amet consectetur.</text></g>
    </svg>
    <span class="brand">Keystead</span>
  </div></section>

  <!-- Row 6 -->
  <section class="slide" style="left:10px;top:868px;width:214px;height:124px;--sx:.2548;--sy:.2583"><div class="stage">
    <div class="abs h-serif" style="left:0;right:0;top:52px;color:#555">FEATURE TIMELINE</div>
    <div class="abs copy" style="left:200px;right:200px;top:88px;text-align:center">Lorem ipsum dolor sit amet of the printing and typesetting.</div>
    <div class="dbl-line" style="top:110px;left:280px;right:280px;height:4px"></div>
    <svg class="abs" style="left:72px;top:136px" width="720" height="320" viewBox="0 0 180 80" font-family="Open Sans">
      <g font-size="2.4" fill="#444" text-anchor="middle"><text x="50" y="5">SUB HEADING</text><text x="95" y="5">SUB HEADING</text><text x="140" y="5">SUB HEADING</text><text x="28" y="60">SUB HEADING</text><text x="73" y="60">SUB HEADING</text><text x="118" y="60">SUB HEADING</text></g>
      <g font-size="2" fill="#999" text-anchor="middle"><text x="50" y="9">Lorem ipsum dolor</text><text x="95" y="9">Lorem ipsum dolor</text><text x="140" y="9">Lorem ipsum dolor</text><text x="28" y="64">Lorem ipsum dolor</text><text x="73" y="64">Lorem ipsum dolor</text><text x="118" y="64">Lorem ipsum dolor</text></g>
      <g stroke="#aaa" stroke-width=".4"><line x1="50" y1="12" x2="50" y2="32"/><line x1="95" y1="12" x2="95" y2="32"/><line x1="140" y1="12" x2="140" y2="32"/><line x1="28" y1="40" x2="28" y2="55"/><line x1="73" y1="40" x2="73" y2="55"/><line x1="118" y1="40" x2="118" y2="55"/></g>
      <rect x="0" y="32" width="22" height="8" fill="#555"/><rect x="22" y="32" width="28" height="8" fill="#7a7a7a"/><rect x="50" y="32" width="28" height="8" fill="var(--red)"/><rect x="78" y="32" width="28" height="8" fill="#e06b3c"/><rect x="106" y="32" width="28" height="8" fill="var(--orange)"/><rect x="134" y="32" width="28" height="8" fill="#f5b041"/><rect x="162" y="32" width="18" height="8" fill="#999"/>
      <g font-size="3.2" fill="#fff" text-anchor="middle"><text x="36" y="37.5">2010</text><text x="64" y="37.5">2011</text><text x="92" y="37.5">2012</text><text x="120" y="37.5">2013</text><text x="148" y="37.5">2014</text><text x="171" y="37.5">2015</text></g>
    </svg>
    <span class="brand">Keystead</span>
  </div></section>

  <section class="slide" style="left:252px;top:868px;width:211px;height:124px;--sx:.2512;--sy:.2583"><div class="stage">
    <div class="abs h-serif" style="left:0;right:0;top:64px">OUR PROJECTS IDEA – 01</div>
    <div class="abs copy" style="left:120px;right:120px;top:100px;text-align:center">Lorem ipsum dolor sit amet, consectetur adipiscing elit semibold.</div>
    <div class="dbl-line" style="top:124px"></div>
    <div class="abs" role="img" aria-label="Interior photo of a modern lobby" style="left:112px;top:156px;width:188px;height:140px;background:linear-gradient(135deg,#6d5a4a,#b9a795)"></div>
    <div class="abs" role="img" aria-label="Interior photo of a red accented office" style="left:328px;top:156px;width:188px;height:140px;background:linear-gradient(135deg,#8b2e2a,#d7d1cb)"></div>
    <div class="abs" role="img" aria-label="Aerial photo of a city district" style="left:544px;top:156px;width:188px;height:140px;background:linear-gradient(135deg,#5c6470,#a6acb3)"></div>
    <div class="abs proj-name" style="left:112px;top:316px;width:188px">PROJECT 1</div>
    <div class="abs proj-name" style="left:328px;top:316px;width:188px">PROJECT 2</div>
    <div class="abs proj-name" style="left:544px;top:316px;width:188px">PROJECT 3</div>
    <div class="abs copy" style="left:120px;top:340px;width:172px;text-align:center">Lorem ipsum dolor sit amet, consectetur adipiscing elit.</div>
    <div class="abs copy" style="left:336px;top:340px;width:172px;text-align:center">Lorem ipsum dolor sit amet, consectetur adipiscing elit.</div>
    <div class="abs copy" style="left:552px;top:340px;width:172px;text-align:center">Lorem ipsum dolor sit amet, consectetur adipiscing elit.</div>
    <span class="brand">Keystead</span>
  </div></section>

  <section class="slide" style="left:491px;top:868px;width:211px;height:124px;--sx:.2512;--sy:.2583"><div class="stage">
    <div class="abs h-serif" style="left:0;right:0;top:64px">OUR PROJECTS IDEA – 2</div>
    <div class="abs copy" style="left:120px;right:120px;top:100px;text-align:center">Lorem ipsum dolor sit amet, consectetur adipiscing elit semibold.</div>
    <div class="dbl-line" style="top:124px"></div>
    <div class="abs" role="img" aria-label="Grid of eight photos of city buildings and skylines" style="left:48px;top:200px;width:792px;height:248px;background:linear-gradient(90deg,#7a6a5a,#2d4670 14%,#5b6f8c 27%,#5a7a3a 40%,#9aa4b2 52%,#314a7a 66%,#b45a3a 80%,#3a5a8a)"></div>
    <span class="brand">Keystead</span>
  </div></section>

  <section class="slide" style="left:738px;top:868px;width:203px;height:124px;--sx:.2417;--sy:.2583"><div class="stage">
    <div class="abs h-serif" style="left:0;right:0;top:64px">OUR PROJECTS IDEA – 2</div>
    <div class="abs copy" style="left:120px;right:120px;top:100px;text-align:center">Lorem ipsum dolor sit amet, consectetur adipiscing elit semibold.</div>
    <div class="dbl-line" style="top:124px"></div>
    <span class="brand">Keystead</span>
  </div></section>

  <section class="slide" style="left:976px;top:868px;width:214px;height:124px;--sx:.2548;--sy:.2583"><div class="stage">
    <div class="abs h-serif" style="left:0;right:0;top:64px">OUR PROJECTS IDEA – 3</div>
    <div class="abs copy" style="left:120px;right:120px;top:100px;text-align:center">Lorem ipsum dolor sit amet, consectetur adipiscing elit semibold.</div>
    <div class="dbl-line" style="top:124px"></div>
    <div class="abs" role="img" aria-label="Photo row of five building exteriors" style="left:72px;top:156px;width:712px;height:84px;background:linear-gradient(90deg,#3e5f8c,#7f95b1 20%,#c8b48a 40%,#4f6f9a 60%,#8a9aaa 80%,#a13a32)"></div>
    <div class="abs" role="img" aria-label="Photo row of five building interiors and towers" style="left:72px;top:292px;width:712px;height:84px;background:linear-gradient(90deg,#5a4632,#a48f74 20%,#2f4f7a 40%,#7d8a9a 60%,#1f2f55 80%,#3c5e9a)"></div>
    <svg class="abs" style="left:72px;top:244px" width="712" height="176" viewBox="0 0 178 44" font-family="Libre Baskerville" text-anchor="middle">
      <g font-size="2.4" fill="#555"><text x="18" y="3">PROJECT 1</text><text x="54" y="3">PROJECT 2</text><text x="90" y="3">PROJECT 3</text><text x="126" y="3">PROJECT 4</text><text x="162" y="3">PROJECT 5</text><text x="18" y="37">PROJECT 6</text><text x="54" y="37">PROJECT 7</text><text x="90" y="37">PROJECT 8</text><text x="126" y="37">PROJECT 9</text><text x="162" y="37">PROJECT 10</text></g>
      <g font-size="1.9" fill="#999" font-family="Open Sans"><text x="18" y="7">Lorem ipsum dolor</text><text x="54" y="7">Lorem ipsum dolor</text><text x="90" y="7">Lorem ipsum dolor</text><text x="126" y="7">Lorem ipsum dolor</text><text x="162" y="7">Lorem ipsum dolor</text><text x="18" y="41">Lorem ipsum dolor</text><text x="54" y="41">Lorem ipsum dolor</text><text x="90" y="41">Lorem ipsum dolor</text><text x="126" y="41">Lorem ipsum dolor</text><text x="162" y="41">Lorem ipsum dolor</text></g>
    </svg>
    <span class="brand">Keystead</span>
  </div></section>
</main>
</body>
</html>
```